Business card logo/design needed

I need a new and fresh business card to get my name out there.
I have made plenty before and have a logo but I dont think it is sending the right message across.
I am a personal trainer running a small online business designed to cut the cost of training by taking it online, allowing you to purchase training over the net, through the help of Skype and video uploads.
You can personalized programs hand written for you or more general programs aimed at your goals.
Our goal is to get everyone to look like and behave like an athlete because there is no point in being in shape if you cant do anything with that body.
I also have a strong background in sports, having played low level college basketball in america and worked as a strength and conditioning coach. I dont like running or slow cardio, I am more focused on weights and functional training for aerobic fitness.
I am young for what I do, but I have lot of knowledge and I need something that says that I am not your standard drill sergeant trainer but someone who will truly help you reach your goals.
My curent logo text is "the climb to the top" but I am not set on that.

Industry/Entity Type

Personal Trainer

Contact Information for Business Card

Desmond Quilby
Summit Forge Motion
Personal trainer
Strength and conditioning coach
0481 552 709
www.summitforgemotion.example

```html
<!DOCTYPE html>
<html lang="en">
<head>
<meta charset="utf-8">
<title>Desmond Quilby – Business Card</title>
<link rel="stylesheet" href="https://fonts.googleapis.com/css2?family=Josefin+Sans:wght@700&family=Yesteryear&family=Oswald:wght@500&display=swap">
<style>
  :root {
    --paper: #eaeaea;
    --ink: #3a3a3a;
    --accent: #ebe625;
    --accent-shade: #d8d31c;
  }
  html, body {
    margin: 0;
    padding: 0;
    overflow: hidden;
    background: var(--paper);
  }
  .card {
    position: relative;
    width: 1200px;
    height: 693px;
    background: var(--paper);
    overflow: hidden;
    font-family: "Josefin Sans", sans-serif;
    color: var(--ink);
  }
  .brand {
    position: absolute;
    left: 282px;
    top: 118px;
    width: 520px;
  }
  .brand-name {
    margin: 0;
    font-family: "Josefin Sans", sans-serif;
    font-weight: 700;
    font-size: 36px;
    letter-spacing: 3px;
    line-height: 1;
    color: var(--ink);
    text-transform: uppercase;
    white-space: nowrap;
  }
  .brand-tagline {
    margin: 10px 0 0 70px;
    padding-top: 6px;
    border-top: 2px solid var(--ink);
    display: inline-block;
    font-family: "Oswald", sans-serif;
    font-weight: 500;
    font-size: 17px;
    letter-spacing: 1.5px;
    text-transform: uppercase;
    color: var(--ink);
  }
  .brand-dot {
    position: absolute;
    left: 817px;
    top: 167px;
    width: 94px;
    height: 94px;
    border-radius: 50%;
    background: var(--accent);
  }
  .person-name {
    position: absolute;
    left: 0;
    width: 1152px;
    top: 316px;
    margin: 0;
    text-align: center;
    font-family: "Yesteryear", cursive;
    font-weight: 400;
    font-size: 62px;
    line-height: 1;
    color: var(--ink);
    text-shadow: 3px 3px 0 var(--accent);
  }
  .role-band {
    position: absolute;
    left: 0;
    top: 389px;
    width: 1200px;
    height: 108px;
    background: var(--accent);
    border-top: 2px solid var(--accent-shade);
    border-bottom: 2px solid var(--accent-shade);
    box-shadow: 0 3px 6px rgba(0,0,0,0.12);
    display: flex;
    align-items: center;
    justify-content: center;
  }
  .role-title {
    margin: 0;
    width: 900px;
    margin-left: -60px;
    text-align: center;
    font-size: 29px;
    line-height: 38px;
    letter-spacing: 0.5px;
    text-transform: uppercase;
    color: var(--ink);
  }
  .contact {
    position: absolute;
    top: 571px;
    display: flex;
    align-items: center;
    gap: 14px;
  }
  .contact-web { left: 172px; }
  .contact-phone { left: 698px; }
  .contact-icon {
    width: 44px;
    height: 44px;
    flex: none;
  }
  .contact-text {
    font-weight: 700;
    color: var(--ink);
    line-height: 1;
    padding-top: 4px;
  }
  .contact-web .contact-text { font-size: 22px; }
  .contact-phone .contact-text { font-size: 31px; letter-spacing: 0.5px; }
</style>
</head>
<body>
<main class="card">
  <header class="brand">
    <h1 class="brand-name">Summit Forge Motion</h1>
    <p class="brand-tagline">The climb to the top</p>
  </header>
  <div class="brand-dot" aria-hidden="true"></div>

  <h2 class="person-name">Desmond Quilby</h2>

  <section class="role-band">
    <p class="role-title">Summit Forge Motion Personal Trainer Strength and Conditioning Coach</p>
  </section>

  <div class="contact contact-web">
    <svg class="contact-icon" viewBox="0 0 44 44" aria-hidden="true">
      <circle cx="22" cy="22" r="22" fill="var(--accent)"/>
      <g fill="none" stroke="#ffffff" stroke-width="3" stroke-linecap="round">
        <rect x="11" y="18" width="13" height="8" rx="4" transform="rotate(-45 17.5 22)"/>
        <rect x="20" y="18" width="13" height="8" rx="4" transform="rotate(-45 26.5 22)"/>
      </g>
    </svg>
    <span class="contact-text">www.summitforgemotion.example</span>
  </div>

  <div class="contact contact-phone">
    <svg class="contact-icon" viewBox="0 0 44 44" aria-hidden="true">
      <circle cx="22" cy="22" r="22" fill="var(--accent)"/>
      <path fill="#ffffff" d="M15.5 11.5c1-.8 2.3-.6 3 .4l2.2 3.3c.6.9.4 2.1-.4 2.8l-1.6 1.3c1 2.3 2.8 4.2 5.1 5.3l1.3-1.6c.7-.8 1.9-1 2.8-.4l3.3 2.2c1 .7 1.2 2 .4 3l-1.3 1.7c-.9 1.1-2.4 1.6-3.8 1.2-6.2-1.9-11-6.7-12.9-12.9-.4-1.4.1-2.9 1.2-3.8z"/>
    </svg>
    <span class="contact-text">0481 552 709</span>
  </div>
</main>
</body>
</html>
```